CD-Cover Desig für neues Album eines Liedermacher-Duos
Zielgruppe
Wir sind ein Liedermacher-Duo und benötigen für unser neues Album mit dem Titel 'Kiesel' ein Cover.
Infos über den Themenbereich der Songs findet man hier: https://www.vorhabenwerk.de/cd-kiesel
Aufgabenstellung
Cover könnte schlicht sein... oder auch kreativ verspielt mit warmen Farben und Formen... aber nicht kitschig.
'Kiesel' im Sinne von Geborgenheit also kein verzehrendes Feuer.. eher sonnig.
Evtl. könnte man unsere beiden Hauptinstrumente (Geige und Gitarre) andeuten.
Sonst stehen auf dem Cover nur noch unsere Namen: Dorothea Lindner & Jörg Haberl

```html
<!DOCTYPE html>
<html lang="de">
<head>
<meta charset="utf-8">
<title>Kiesel – Dorothea Lindner &amp; Jörg Haberl</title>
<link rel="stylesheet" href="https://fonts.googleapis.com/css2?family=Comfortaa:wght@300&family=Roboto:wght@500&display=swap">
<style>
  :root {
    --page: #ffffff;
    --wine: #9a2a3a;
    --crimson: #b13a3c;
    --rust: #c4563a;
    --amber: #d9803f;
    --honey: #e8a25a;
    --title: #ece6e2;
    --names: #f4ece6;
  }
  * { margin: 0; padding: 0; box-sizing: border-box; }
  html, body {
    width: 1200px;
    height: 1200px;
    overflow: hidden;
    background: var(--page);
  }
  .canvas {
    position: relative;
    width: 1200px;
    height: 1200px;
  }
  .cover {
    position: absolute;
    left: 244px;
    top: 244px;
    width: 713px;
    height: 713px;
    overflow: hidden;
  }
  .cover-photo {
    position: absolute;
    inset: 0;
    width: 100%;
    height: 100%;
  }
  .album-title {
    position: absolute;
    right: 54px;
    top: 58px;
    font-family: "Comfortaa", "Quicksand", sans-serif;
    font-weight: 300;
    font-size: 118px;
    line-height: 1;
    letter-spacing: 2px;
    color: var(--title);
    text-transform: uppercase;
  }
  .artists {
    position: absolute;
    right: 54px;
    top: 200px;
    font-family: "Roboto", Arial, sans-serif;
    font-weight: 500;
    font-size: 20.5px;
    line-height: 1;
    color: var(--names);
    white-space: nowrap;
  }
</style>
</head>
<body>
  <main class="canvas">
    <section class="cover">
      <svg class="cover-photo" viewBox="0 0 713 713" preserveAspectRatio="none"
           role="img" aria-label="Warm getöntes Foto: Geige mit Bogen, auf einer Hand liegend, überblendet mit dem Griffbrett einer Gitarre">
        <defs>
          <linearGradient id="base-tone" x1="0" y1="0" x2="1" y2="1">
            <stop offset="0" stop-color="var(--rust)"/>
            <stop offset="0.35" stop-color="var(--crimson)"/>
            <stop offset="0.7" stop-color="var(--wine)"/>
            <stop offset="1" stop-color="var(--crimson)"/>
          </linearGradient>
          <radialGradient id="warm-glow" cx="0.62" cy="0.6" r="0.55">
            <stop offset="0" stop-color="var(--honey)" stop-opacity="0.85"/>
            <stop offset="0.55" stop-color="var(--amber)" stop-opacity="0.45"/>
            <stop offset="1" stop-color="var(--amber)" stop-opacity="0"/>
          </radialGradient>
        </defs>
        <rect width="713" height="713" fill="url(#base-tone)"/>
        <rect width="713" height="713" fill="url(#warm-glow)"/>
      </svg>
      <h1 class="album-title">Kiesel</h1>
      <p class="artists">Dorothea Lindner &amp; Jörg Haberl</p>
    </section>
  </main>
</body>
</html>
```